Business Card Design Project

Vexrida will provide 3D analysis of remote sensing digital data sets of airborne (aircraft/UAV) and satellite data in order to deliver 3D geospatial mapping information, videos and augmented reality products. Typical high end customers are military and security related customers, line object infrastructure owners or providers (pipelines gas/oil/fuel/water, energy lines, borders, coastal zones and rivers, transportation roads on the sea, roads, and railway systems). All these potential customers are linked to regular service monitoring, surveillance and reconnaissance covering cities, counties and countries. The company will provide 3D presentation of infrastructure (which is likely to become a binding requirement in Europe and other countries), disaster prevention and monitoring.

Target Market(s)

Target market are US based governmental agencies, such as Bureau of Civic Resilience, Federal Terrain Insight office, Ministy of Frontier Works, Bureau of Lands/Federal Terrain Registry, etc as well as commercial entities like gas, utilities, etc > Primary services will be to provide 3D geospatial mapping to support search & rescue, border control, infrastructure (pipeline, electric wires, etc.) management, agriculture, climate control, etc.

Industry/Entity Type

Business

Contact Information for Business Card

Vincent Renz6 Gristmill RdCedar Knolls, NJ 079271-973-652-8379vrenz.straight4ward@gmail.com

Requirements
Must have
• Business card must have the company logo (provided) - and want to keep with the colors in the logo

```html
<!DOCTYPE html>
<html lang="en">
<head>
<meta charset="utf-8">
<title>Vexrida business card</title>
<link rel="stylesheet" href="https://fonts.googleapis.com/css2?family=Mulish:wght@300;400;700&display=swap">
<style>
  :root {
    --backdrop: #2e2e2e;
    --card: #ffffff;
    --brand-blue: #0f4c66;
    --brand-red: #e0283a;
    --ink-grey: #6b6f73;
  }
  * { margin: 0; padding: 0; box-sizing: border-box; }
  html, body {
    width: 1200px;
    height: 659px;
    overflow: hidden;
    background: var(--backdrop);
    font-family: "Mulish", sans-serif;
  }
  .stage {
    position: relative;
    width: 1200px;
    height: 659px;
    display: flex;
    align-items: center;
    justify-content: center;
    gap: 60px;
  }
  .card {
    position: relative;
    width: 500px;
    height: 286px;
    background: var(--card);
    overflow: hidden;
  }

  /* Front: contact side */
  .card-front .edge-band {
    position: absolute;
    top: 0;
    right: 0;
    width: 34px;
    height: 100%;
    background: var(--brand-blue);
  }
  .card-front .wordmark {
    position: absolute;
    top: 44px;
    right: 70px;
    font-size: 54px;
    font-weight: 300;
    color: var(--brand-blue);
    letter-spacing: 1px;
  }
  .contact {
    position: absolute;
    left: 34px;
    bottom: 34px;
    color: var(--ink-grey);
    font-size: 11.5px;
    font-weight: 400;
    line-height: 1.55;
  }
  .contact .person-name {
    font-size: 17px;
    font-weight: 700;
    color: var(--brand-blue);
    margin-bottom: 4px;
  }
  .contact .address { margin-bottom: 6px; }
  .contact .line {
    display: flex;
    align-items: center;
    gap: 7px;
  }
  .contact .line svg {
    width: 10px;
    height: 10px;
    flex: none;
    fill: var(--brand-blue);
  }

  /* Back: logo side */
  .card-back {
    display: flex;
    align-items: center;
    justify-content: center;
  }
  .card-back .wordmark {
    font-size: 56px;
    font-weight: 300;
    color: var(--brand-blue);
    letter-spacing: 2px;
  }
</style>
</head>
<body>
<main class="stage">
  <section class="card card-front" aria-label="Business card front">
    <div class="wordmark">Vexrida</div>
    <div class="edge-band"></div>
    <div class="contact">
      <p class="person-name">Marcus Doyle</p>
      <p class="address">14 Larkspur Ln<br>Pine Hollow, NJ 07044</p>
      <p class="line">
        <svg viewBox="0 0 10 10" aria-hidden="true"><path d="M2 0.5 L3.6 0.5 L4.2 3 L3 3.8 Q4 6 6.2 7 L7 5.8 L9.5 6.4 L9.5 8 Q9.5 9.5 8 9.5 Q0.5 9 0.5 2 Q0.5 0.5 2 0.5Z"/></svg>
        973-555-0142
      </p>
      <p class="line">
        <svg viewBox="0 0 10 10" aria-hidden="true"><path d="M0.5 2 H9.5 V8.5 H0.5Z M1.2 2.6 L5 5.6 L8.8 2.6" fill="none" stroke="#0f4c66" stroke-width="1"/></svg>
        mdoyle.brightpath7@mailvista.example
      </p>
      <p class="line">
        <svg viewBox="0 0 10 10" aria-hidden="true"><circle cx="5" cy="5" r="4.5"/><path d="M0.5 5 H9.5 M5 0.5 Q2.5 5 5 9.5 M5 0.5 Q7.5 5 5 9.5" fill="none" stroke="#ffffff" stroke-width="0.7"/></svg>
        www.vexrida.example
      </p>
    </div>
  </section>

  <section class="card card-back" aria-label="Business card back">
    <div class="wordmark">Vexrida</div>
  </section>
</main>
</body>
</html>
```